Slogan Project - City tour.

I need a slogan/catch frase for "Lumen Path Outings"
Like "Lumen Path Outings - Let's discover together"

to organize daily city tours to visit different part of the city or museums.

```html
<!DOCTYPE html>
<html lang="en">
<head>
<meta charset="UTF-8">
<title>Lumen Path Outings — Slogan</title>
<link rel="preconnect" href="https://fonts.googleapis.com">
<link href="https://fonts.googleapis.com/css2?family=Lexend+Exa:wght@500;600&display=swap" rel="stylesheet">
<style>
  :root {
    --paper: #ffffff;
    --band: #000000;
    --ink-light: #ffffff;
  }
  html, body {
    margin: 0;
    padding: 0;
    overflow: hidden;
    background: var(--paper);
  }
  .canvas {
    position: relative;
    width: 1200px;
    height: 927px;
    background: var(--paper);
    overflow: hidden;
    font-family: "Lexend Exa", "Helvetica Neue", Arial, sans-serif;
  }
  .hero-band {
    position: absolute;
    left: 0;
    top: 133px;
    width: 1200px;
    height: 529px;
    background: var(--band);
  }
  .brand-title {
    position: absolute;
    left: 14px;
    right: 0;
    top: 48px;
    margin: 0;
    text-align: center;
    white-space: nowrap;
    color: var(--ink-light);
    font-weight: 600;
    font-size: 60px;
    line-height: 1;
    letter-spacing: 0.01em;
    text-transform: uppercase;
  }
  .tagline {
    position: absolute;
    left: 14px;
    right: 0;
    top: 238px;
    margin: 0;
    text-align: center;
    white-space: nowrap;
    color: var(--ink-light);
    font-weight: 500;
    font-size: 28px;
    line-height: 1;
    letter-spacing: 0.01em;
    text-transform: uppercase;
  }
</style>
</head>
<body>
  <main class="canvas">
    <section class="hero-band">
      <h1 class="brand-title">Lumen Path Outings</h1>
      <p class="tagline">“Its simply amazing”</p>
    </section>
  </main>
</body>
</html>
```